Pipe and Drape Company Web site

Name of client is "Lumen Curtain" with a tagline of, "Fine Fabric, Finer Care." which will need to go across the middle of the header area. Logo will be on the left. Connectors on the right. Connectors being, join newsletter, facebook, twitter, linked In, etc...

Please refer to www.folvarstage.example for feel and layout and then www.tolmerhawks.example for background imagery style and preferred color scheme. Colors for the site should be black and dark purple with sub page text areas being white with black text. Yet still surrounded with black framing and purple infused background. We'll need a Large impactful main image area to display scrolling images. Below that will be 4 content area boxes with each of the following titles. "Corporate Events" , "Weddings" , "Special Events" , and "Products".

Main nav will need to be across the top of main image and include the 5 following tabs: "Lumen Experience", "DrapeRental" , "Gallery" , "Resources" ,
"Contact Us". Also leave a blank space on the right end of main nav in case we decide to add a 6th main nav at a later date.

This is a nationwide company and is a leader in their industry. The site should look very high end and classy. Highest quality and largest selection of drape anywhere. It should convey dependability, professionalism, Trustworthy, and expertise.

The main calls to action should be to get the visitor to call the phone number, or contact via email.

Main visitor demographic will be female event coordinators.

Sub Page design will vary based on the market segment chosen from home page. However, we feel the "wedding" category would be a good option since those pages might have a lighter look and feminine feel to them. Be sure to make it simple for the visitor to go back from the sub page, to the hame page via nav choices, or market segment boxes across the bottom again.

```html
<!DOCTYPE html>
<html lang="en">
<head>
<meta charset="utf-8">
<title>Lumen Curtain — Pipe and Drape</title>
<link rel="stylesheet" href="https://fonts.googleapis.com/css2?family=Arimo:ital,wght@0,400;0,700;1,700&family=EB+Garamond:wght@500&family=Noto+Sans&family=Ubuntu&display=swap">
<style>
:root{
  --night:#0a0612;
  --violet-deep:#2c0d3d;
  --violet:#4a1a63;
  --violet-mid:#6b2a8a;
  --lilac:#a57fbf;
  --lilac-soft:#c9a9dc;
  --ink:#2a2a2a;
  --body-grey:#555;
  --link:#6a1b9a;
  --white:#fff;
  --black:#000;
}
*{box-sizing:border-box;margin:0;padding:0}
html,body{width:1200px;height:1172px;overflow:hidden}
body{
  position:relative;
  font-family:"Arimo",Arial,sans-serif;
  background:var(--night);
}
.backdrop{
  position:absolute;inset:0;
  background:
    radial-gradient(ellipse 420px 300px at 1020px 60px,rgba(150,70,200,.55),transparent 70%),
    radial-gradient(ellipse 380px 420px at 120px 260px,rgba(110,60,180,.55),transparent 70%),
    radial-gradient(ellipse 700px 260px at 600px 1000px,rgba(170,120,40,.55),transparent 70%),
    linear-gradient(180deg,#1d1240 0%,#2a1550 35%,#1a0d2c 60%,#3a2510 85%,#120a05 100%);
}
.frame{position:absolute;left:175px;top:150px;width:850px;height:1022px;background:var(--black)}

/* header */
.logo{
  position:absolute;left:182px;top:7px;width:217px;height:68px;
  border:2px solid var(--white);border-radius:8px;background:rgba(0,0,0,.55);
  display:flex;align-items:center;justify-content:center;
  color:var(--white);font-size:27px;font-weight:400;letter-spacing:.5px;white-space:nowrap;
}
.tagline{
  position:absolute;left:497px;top:5px;width:230px;
  font-family:"EB Garamond",Georgia,serif;font-size:22px;line-height:26px;color:var(--white);
}
.tagline span{display:block}
.tagline span+span{padding-left:44px}
.connectors{position:absolute;left:833px;top:42px;display:flex;gap:6px}
.connector{
  width:33px;height:33px;border-radius:6px;
  background:linear-gradient(180deg,#7cc0ec,#2a6fb3);border:1px solid #cfe6f7;
  color:var(--white);font-size:8px;font-weight:700;
  display:flex;align-items:center;justify-content:center;text-align:center;line-height:9px;
}

/* nav */
.main-nav{
  position:absolute;left:163px;top:92px;width:874px;height:70px;
  border-radius:14px 14px 10px 10px;
  background:linear-gradient(180deg,#6b2487 0%,#4d1366 45%,#2e0a3f 100%);
}
.main-nav ul{list-style:none;display:flex;height:46px;margin-left:27px}
.main-nav li{
  display:flex;align-items:center;padding:0 14px;
  color:var(--white);font-size:18px;white-space:nowrap;
  border-right:1px solid rgba(255,255,255,.35);
}
.nav-inset{position:absolute;left:12px;right:12px;top:46px;bottom:0;background:var(--black);border-radius:6px 6px 0 0}

/* slider */
.showcase{
  position:absolute;left:185px;top:160px;width:830px;height:532px;
  background:var(--white);border-radius:12px;
}
.showcase-image{
  position:absolute;left:10px;top:10px;width:810px;height:495px;border-radius:8px;
  background:
    radial-gradient(ellipse 200px 120px at 300px 90px,rgba(255,230,170,.8),transparent 70%),
    linear-gradient(180deg,#6a4a2a 0%,#b88a4e 35%,#d9b070 60%,#8a6a40 80%,#3a2a2a 100%);
}
.dots{position:absolute;left:0;right:0;top:515px;display:flex;justify-content:center;gap:11px}
.dot{width:10px;height:10px;border-radius:50%;background:#4a2a5e}
.dot.is-active{background:var(--black)}

/* content panel */
.content{
  position:absolute;left:185px;top:702px;width:830px;height:480px;
  background:var(--white);border-radius:12px 12px 0 0;
}
.welcome{position:absolute;left:13px;top:8px;width:548px}
.welcome h1{font-size:18px;font-weight:400;color:var(--violet-deep)}
.welcome p{
  margin-top:10px;font-family:"Noto Sans",Verdana,sans-serif;font-size:12.2px;line-height:18px;
  color:var(--body-grey);text-align:justify;letter-spacing:.2px;
}
.read-more{
  display:flex;align-items:center;justify-content:flex-end;gap:6px;white-space:nowrap;
  font-family:"Noto Sans",Verdana,sans-serif;font-size:13px;color:var(--link);letter-spacing:.3px;
}
.welcome .read-more{margin-top:6px}

.segment-tabs{position:absolute;left:42px;top:160px;display:flex;gap:11px}
.tab{
  height:33px;padding:0 6px;border-radius:8px 8px 0 0;
  display:flex;align-items:center;justify-content:center;white-space:nowrap;
  font-size:13.5px;font-weight:700;font-style:italic;color:var(--white);
  background:linear-gradient(180deg,#8a5aa8,#6a3a88);
}
.tab.is-active{background:linear-gradient(180deg,#7b4f99,#5b2f78);color:var(--black)}
.tab:nth-child(1){width:140px}
.tab:nth-child(2){width:139px}
.tab:nth-child(3){width:139px}

.segment-panel{
  position:absolute;left:10px;top:191px;width:551px;height:219px;
  border:4px solid var(--lilac);border-radius:20px;padding:16px 16px 0 15px;
}
.segment-photo{
  float:left;width:94px;height:94px;margin:0 18px 4px 0;border:1px solid #bbb;
  background:linear-gradient(160deg,#3a3a3a,#8a7a70 50%,#e8e2da);
}
.segment-panel p{
  font-family:"Noto Sans",Verdana,sans-serif;font-size:12px;line-height:18.2px;
  color:var(--body-grey);text-align:justify;letter-spacing:.1px;
}
.segment-panel .read-more{position:absolute;right:14px;bottom:10px}

/* sidebar */
.side-box{
  position:absolute;left:590px;width:230px;
  background:var(--violet-deep);border:2px solid #9a5ec0;border-radius:8px;overflow:hidden;
}
.side-box h2{
  height:38px;display:flex;align-items:center;justify-content:center;
  font-family:"Ubuntu",Arial,sans-serif;font-weight:400;font-size:21px;color:var(--white);
  background:linear-gradient(180deg,#9a6ab8 0%,#5c2b7a 100%);
  border-radius:0 0 50% 50% / 0 0 8px 8px;
}
.contact-box{top:10px;height:140px}
.contact-line{display:flex;align-items:center;gap:14px;margin-left:11px;color:var(--white);font-family:"Ubuntu",Arial,sans-serif;white-space:nowrap}
.contact-line svg,.phone-icon{flex-shrink:0}
.contact-line.phone{margin-top:10px;font-size:22px;letter-spacing:.5px}
.contact-line.email{margin-top:14px;font-size:17px}
.phone-icon{width:32px;height:32px;border-radius:50%;background:radial-gradient(circle at 40% 35%,#fff,#999);display:flex;align-items:center;justify-content:center}
.products-box{top:160px;height:250px}
.product{position:relative;margin:14px 10px 0 25px;color:var(--white)}
.product h3{font-size:14.5px;font-weight:400}
.product h3::before{content:"›";position:absolute;left:-14px;top:-2px;font-size:16px}
.product p{margin-top:4px;font-size:10px;line-height:13px}
.divider{margin:12px 10px 0;border-top:1px dotted rgba(255,255,255,.6)}
.products-box .more{position:absolute;right:10px;bottom:12px;font-size:11px;font-weight:700;font-style:italic;color:var(--white);text-decoration:underline}

/* footer */
.footer{position:absolute;left:10px;top:424px;width:810px;border-top:2px dotted #999}
.footer-nav{position:absolute;left:0;top:12px;font-size:11px;color:var(--ink);display:flex;gap:8px;white-space:nowrap}
.footer-nav a{color:inherit;text-decoration:none}
.footer-nav a:first-child{color:var(--link)}
.footer-nav i{font-style:normal}
.copyright{position:absolute;right:0;top:12px;font-size:11px;color:var(--ink);white-space:nowrap}
.copyright b{font-weight:400;color:var(--link)}
</style>
</head>
<body>
<div class="backdrop" role="img" aria-label="Starry purple night sky over a glowing golden field"></div>
<div class="frame"></div>

<header>
  <div class="logo">Lumen Curtain</div>
  <div class="tagline"><span>"Fine Fabric,</span><span>Finer Care."</span></div>
  <div class="connectors">
    <div class="connector">Blog</div>
    <div class="connector">News</div>
    <div class="connector">Post</div>
    <div class="connector">Net</div>
    <div class="connector">Fans</div>
  </div>
</header>

<nav class="main-nav">
  <ul>
    <li>Lumen Experience</li>
    <li>DrapeRental</li>
    <li>Gallery</li>
    <li>Resources</li>
    <li>Contact Us</li>
  </ul>
  <div class="nav-inset"></div>
</nav>

<section class="showcase">
  <div class="showcase-image" role="img" aria-label="Grand ballroom with gold drapes, chandelier and rows of set conference tables"></div>
  <div class="dots"><span class="dot is-active"></span><span class="dot"></span><span class="dot"></span><span class="dot"></span></div>
</section>

<main class="content">
  <section class="welcome">
    <h1>Welcome To Lumen Curtain</h1>
    <p>Lorem Ipsum is simply dummy text of the printing and typesetting industry. Lorem Ipsum has been the industry's standard dummy text ever since the 1500s, when an unknown printer took a galley of type and scrambled it to make a type specimen book. It has survived not only five centuries, but also the leap into electronic typesetting, remaining essentially unchanged. It was popularised in the 1960s</p>
    <div class="read-more">
      <svg width="15" height="15" viewBox="0 0 16 16"><circle cx="8" cy="8" r="8" fill="#6a1b9a"/><path d="M4 8.3l2.7 2.6L12 5.5" stroke="#fff" stroke-width="2" fill="none"/></svg>Read More...
    </div>
  </section>

  <div class="segment-tabs">
    <div class="tab is-active">Corporate Events</div>
    <div class="tab">Weddings Events</div>
    <div class="tab">Special&nbsp; Events</div>
  </div>
  <section class="segment-panel">
    <div class="segment-photo" role="img" aria-label="Guests raising glasses in a toast at an event"></div>
    <p>Lorem Ipsum is simply dummy text of the printing and typesetting industry. Lorem Ipsum has been the industry's standard dummy text ever since the 1500s, when an unknown printer took a galley of type and scrambled it to make a type specimen book. It has survived not only five centuries, but also the leap into electronic typesetting, remaining essentially unchanged. It was popularised in Lorem Ipsum is simply dummy text of the printing and typesetting industry. Lorem Ipsum has been the industry's standard dummy text ever since the 1500s, when an unknown printer took a galley of type and scrambled it to make a type specimen</p>
    <div class="read-more">
      <svg width="15" height="15" viewBox="0 0 16 16"><circle cx="8" cy="8" r="8" fill="#6a1b9a"/><path d="M4 8.3l2.7 2.6L12 5.5" stroke="#fff" stroke-width="2" fill="none"/></svg>Read More...
    </div>
  </section>

  <aside class="side-box contact-box">
    <h2>Contact Us</h2>
    <div class="contact-line phone">
      <span class="phone-icon"><svg width="18" height="14" viewBox="0 0 18 14"><path d="M1 5c0-3 16-3 16 0v2h-4V5H5v2H1z" fill="#222"/><rect x="5" y="7" width="8" height="6" rx="1" fill="#222"/></svg></span>04417 - 20386
    </div>
    <div class="contact-line email">
      <svg width="30" height="20" viewBox="0 0 30 20"><rect width="30" height="20" rx="2" fill="#e8e8ec"/><path d="M1 1l14 11L29 1" stroke="#aaa" fill="none"/></svg>info@lumen.example
    </div>
  </aside>

  <aside class="side-box products-box">
    <h2>Products</h2>
    <div class="product-list">
      <div class="product">
        <h3>Name of The Product Lorem</h3>
        <p>Lorem Ipsum is simply dummy text of the printing and typesetting. Lorem Ipsum has been the industry's</p>
      </div>
      <div class="divider"></div>
      <div class="product">
        <h3>Name of The Product Lorem</h3>
        <p>Lorem Ipsum is simply dummy text of the printing and typesetting. Lorem Ipsum has been the industry's standard dummy text ever since</p>
      </div>
    </div>
    <span class="more">Read More</span>
  </aside>

  <footer class="footer">
    <div class="footer-nav">
      <a>Lumen Experience</a><i>|</i><a>DrapeRental</a><i>|</i><a>Gallery</a><i>|</i><a>Resources</a><i>|</i><a>Contact Us</a>
    </div>
    <div class="copyright">Copyright © 2011 <b>Lumen Curtain</b>. All Rights Reserved.</div>
  </footer>
</main>
</body>
</html>
```